Recommend a friend FLYER - Brisk Window Cleaning

Window cleaning company with focus on quality of service and professionalism. Friendly, relaxed tone, and simple clear communications.

Target Market(s)

Homeowners with moderate income

Industry/Entity Type

Window Cleaning

Font styles to use
Serif
Decorative

Colors
33a6d7
fbee3d
faa54b
d3d3d3

```html
<!DOCTYPE html>
<html lang="en">
<head>
<meta charset="utf-8">
<title>Recommend a Friend Flyer – Brisk Window Cleaning</title>
<link rel="stylesheet" href="https://fonts.googleapis.com/css2?family=Questrial&family=Cormorant+Garamond:wght@500&family=Satisfy&display=swap">
<style>
  :root {
    --stage: #3a3a3a;
    --sky-pale: #f4f9fd;
    --sky-light: #d6ebf8;
    --sky-mid: #a9d5f0;
    --brand-blue: #33a6d7;
    --navy: #1f3f8f;
    --ink: #1a1a1a;
    --rule: #2a3f80;
  }
  * { box-sizing: border-box; margin: 0; padding: 0; }
  html, body { width: 1200px; height: 900px; overflow: hidden; }
  body { background: var(--stage); font-family: "Questrial", Arial, sans-serif; position: relative; }

  .flyer { position: absolute; top: 110px; width: 490px; height: 694px; overflow: hidden; }
  .flyer--front { left: 68px; background: linear-gradient(180deg, var(--sky-pale), var(--sky-light) 60%, var(--sky-pale)); }
  .flyer--back { left: 641px; background: linear-gradient(180deg, var(--sky-light), var(--sky-mid) 70%, var(--sky-light)); }
  .waves { position: absolute; inset: 0; }

  .mascot { position: absolute; left: 305px; top: 45px; width: 170px; height: 208px;
    border-radius: 50% 50% 42% 42%;
    background: radial-gradient(circle at 50% 42%, #6fcdf0, #3aa7dc 75%); opacity: .85; }

  .front-line { position: absolute; color: var(--ink); font-size: 36px; line-height: 1; white-space: nowrap; }
  .front-line--refer { left: 50px; top: 182px; }
  .front-line--to { left: 50px; top: 230px; }

  .brand { position: absolute; color: var(--navy); font-family: "Questrial", Arial, sans-serif; display: flex; align-items: center; white-space: nowrap; }
  .brand__mark { background: var(--brand-blue); flex: none; }
  .brand--front { left: 52px; top: 272px; gap: 16px; }
  .brand--front .brand__name { font-size: 88px; line-height: .9; }
  .brand--front .brand__sub { font-size: 27px; line-height: 1.1; }
  .brand--front .brand__mark { width: 56px; height: 56px; }
  .brand--back { left: 0; right: 0; top: 100px; justify-content: center; gap: 12px; }
  .brand--back .brand__name { font-size: 50px; line-height: .9; }
  .brand--back .brand__sub { font-size: 15px; }
  .brand--back .brand__mark { width: 32px; height: 32px; }

  .offer { position: absolute; left: 0; right: 0; text-align: center; white-space: nowrap; }
  .offer--get { top: 405px; font-size: 34px; color: var(--ink); }
  .offer--voucher { top: 452px; font-family: "Cormorant Garamond", Georgia, serif; font-weight: 500; font-size: 66px; color: var(--brand-blue); }
  .offer--asa { top: 540px; font-family: "Cormorant Garamond", Georgia, serif; font-weight: 500; font-size: 36px; color: var(--navy); }
  .offer--little { top: 592px; font-size: 21px; color: var(--ink); }
  .offer--from { top: 636px; font-size: 32px; color: var(--navy); }

  .thanks { position: absolute; top: 40px; left: 0; right: 0; text-align: center; white-space: nowrap;
    font-family: "Satisfy", cursive; font-size: 26px; color: var(--ink); }

  .form { position: absolute; left: 76px; top: 210px; width: 336px; color: var(--navy); font-size: 14.5px; }
  .form__heading { position: absolute; left: 0; }
  .field { position: absolute; left: 0; right: 0; display: flex; align-items: flex-end; gap: 6px; white-space: nowrap; }
  .field__rule { flex: 1; border-bottom: 1px solid var(--rule); height: 1px; margin-bottom: 3px; }
  .field--cont { left: 61px; }

  .terms { position: absolute; left: 80px; width: 330px; top: 576px; text-align: center;
    color: var(--navy); font-size: 15px; line-height: 20px; }
</style>
</head>
<body>
  <section class="flyer flyer--front">
    <svg class="waves" viewBox="0 0 490 694" aria-hidden="true">
      <path d="M0 160 Q245 80 490 120 L490 0 L0 0Z" fill="#ffffff" opacity=".55"/>
      <path d="M0 480 Q260 380 490 450 L490 560 Q250 500 0 600Z" fill="#ffffff" opacity=".5"/>
      <path d="M0 640 Q260 600 490 650 L490 694 L0 694Z" fill="#ffffff" opacity=".6"/>
    </svg>
    <div class="mascot" role="img" aria-label="Cartoon blue bird mascot shouting through a megaphone"></div>
    <p class="front-line front-line--refer">Refer A Friend</p>
    <p class="front-line front-line--to">To</p>
    <div class="brand brand--front">
      <div>
        <div class="brand__name">Brisk</div>
        <div class="brand__sub">Window Cleaning</div>
      </div>
      <span class="brand__mark"></span>
    </div>
    <p class="offer offer--get">and get a</p>
    <p class="offer offer--voucher">£10 voucher</p>
    <p class="offer offer--asa">as a</p>
    <p class="offer offer--little">little</p>
    <p class="offer offer--from">From Us!</p>
  </section>

  <section class="flyer flyer--back">
    <svg class="waves" viewBox="0 0 490 694" aria-hidden="true">
      <path d="M0 170 Q245 210 490 150 L490 0 L0 0Z" fill="#ffffff" opacity=".35"/>
      <path d="M0 420 Q250 360 490 420 L490 500 Q250 450 0 520Z" fill="#ffffff" opacity=".25"/>
    </svg>
    <p class="thanks">Thank you for your loyal support</p>
    <div class="brand brand--back">
      <div>
        <div class="brand__name">Brisk</div>
        <div class="brand__sub">Window Cleaning</div>
      </div>
      <span class="brand__mark"></span>
    </div>
    <div class="form">
      <p class="form__heading" style="top:0">Your Details:</p>
      <div class="field" style="top:38px"><span>Name:</span><span class="field__rule"></span></div>
      <div class="field" style="top:77px"><span>Address:</span><span class="field__rule"></span></div>
      <div class="field field--cont" style="top:124px"><span class="field__rule"></span></div>
      <p class="form__heading" style="top:158px">Your Friend’s Details:</p>
      <div class="field" style="top:196px"><span>Name:</span><span class="field__rule"></span></div>
      <div class="field" style="top:235px"><span>Address:</span><span class="field__rule"></span></div>
      <div class="field field--cont" style="top:282px"><span class="field__rule"></span></div>
      <div class="field" style="top:314px"><span>Telephone No:</span><span class="field__rule"></span></div>
    </div>
    <p class="terms">You will receive a £10 voucher redeemable against any of our services, on completion of your friend’s first clean. Must be within the areas we cover.</p>
  </section>
</body>
</html>
```